Business card - fitness trainer

Hello all, we have the need for a business card and would like to work with you to utilize your skills.

We would like the background to be black and use elements of the logo and lettering in blue, yellow and white, if that is possible.

Please see the attached logo which we would like to incorporate.

http://www.plinvarto.example/download-source-file.aspx?designid=5830416&type=source

I am having a hard time attaching the logo files so please let me know if you cannot see it

Thank you

Fitness

```html
<!DOCTYPE html>
<html lang="en">
<head>
<meta charset="utf-8">
<title>Vello Health and Fitness – Business Card</title>
<link href="https://fonts.googleapis.com/css2?family=Questrial&display=swap" rel="stylesheet">
<style>
  :root {
    --stage: #1a1a1a;
    --card-dark: #1f1f21;
    --card-dark-edge: #2c2c2f;
    --card-light: #ffffff;
    --gold: #f5b335;
    --blue: #1f7cc4;
    --text-light: #e6e6e6;
  }
  * { box-sizing: border-box; margin: 0; padding: 0; }
  html, body {
    width: 1200px; height: 871px; overflow: hidden;
    background: var(--stage);
    font-family: "Questrial", "Century Gothic", sans-serif;
  }
  .stage { position: relative; width: 1200px; height: 871px; }

  .card {
    position: absolute;
    width: 560px; height: 320px;
    border-radius: 4px;
    overflow: hidden;
    box-shadow: 0 18px 40px rgba(0,0,0,.55);
  }

  /* Back side */
  .card--back {
    left: 110px; top: 100px;
    background: linear-gradient(160deg, var(--card-dark-edge), var(--card-dark) 60%);
    color: var(--text-light);
  }
  .brand {
    position: absolute;
    display: flex; align-items: center; gap: 12px;
  }
  .brand__dot { width: 34px; height: 34px; border-radius: 50%; flex: none; }
  .brand__words { display: flex; flex-direction: column; line-height: 1; }
  .brand__name { font-size: 64px; letter-spacing: 1px; }
  .brand__tag { font-size: 11px; letter-spacing: 1px; margin-top: 2px; }

  .card--back .brand { left: 160px; top: 60px; }
  .card--back .brand__dot { background: var(--gold); }
  .card--back .brand__name,
  .card--back .brand__tag { color: var(--gold); }

  .contact {
    position: absolute; right: 34px; top: 170px;
    list-style: none; font-size: 19px; letter-spacing: 1.5px;
  }
  .contact li { display: flex; align-items: center; gap: 10px; margin-bottom: 6px; }
  .address {
    position: absolute; left: 40px; bottom: 40px;
    font-size: 19px; letter-spacing: 1.5px; line-height: 1.25;
    font-style: normal;
    display: flex; gap: 10px; align-items: flex-start;
  }
  .icon { width: 16px; height: 16px; flex: none; fill: var(--gold); }

  /* Front side */
  .card--front {
    left: 540px; top: 451px;
    background: var(--card-light);
  }
  .card--front .brand { left: 36px; top: 22px; }
  .card--front .brand__dot { background: var(--gold); width: 28px; height: 28px; }
  .card--front .brand__name { font-size: 56px; color: var(--blue); }
  .card--front .brand__tag { font-size: 10px; color: var(--blue); }
  .stripes { position: absolute; inset: 0; width: 100%; height: 100%; }
  .identity {
    position: absolute; right: 34px; bottom: 30px; text-align: left;
    letter-spacing: 3px; line-height: 1.1;
  }
  .identity__name { font-size: 30px; color: var(--gold); font-weight: 400; }
  .identity__role { font-size: 24px; color: var(--blue); }
</style>
</head>
<body>
<main class="stage">

  <section class="card card--back" aria-label="Business card back">
    <div class="brand">
      <span class="brand__dot"></span>
      <span class="brand__words">
        <span class="brand__name">vello</span>
        <span class="brand__tag">HEALTH AND FITNESS</span>
      </span>
    </div>

    <ul class="contact">
      <li>
        <svg class="icon" viewBox="0 0 16 16"><rect x="3" y="1" width="10" height="14" rx="2" fill="none" stroke="#f5b335" stroke-width="1.8"/></svg>
        (0) 41 555 01 23
      </li>
      <li>
        <svg class="icon" viewBox="0 0 16 16"><path d="M1 4h14v9H1z M1 4l7 5 7-5" fill="none" stroke="#f5b335" stroke-width="1.8"/></svg>
        danakessler@mailbox.example
      </li>
    </ul>

    <address class="address">
      <svg class="icon" viewBox="0 0 16 16"><path d="M8 1L1 8h2v7h4v-4h2v4h4V8h2z"/></svg>
      <span>Sample address 766<br>&nbsp;Sample Town 01234</span>
    </address>
  </section>

  <section class="card card--front" aria-label="Business card front">
    <svg class="stripes" viewBox="0 0 560 320" preserveAspectRatio="none" aria-hidden="true">
      <polygon points="0,150 560,36 560,50 0,164" fill="var(--gold)"/>
      <polygon points="0,190 560,76 560,112 0,226" fill="var(--blue)"/>
    </svg>
    <div class="brand">
      <span class="brand__dot"></span>
      <span class="brand__words">
        <span class="brand__name">vello</span>
        <span class="brand__tag">HEALTH AND FITNESS</span>
      </span>
    </div>
    <div class="identity">
      <h1 class="identity__name">DANA KESSLER</h1>
      <p class="identity__role">FITNESS TRAINER</p>
    </div>
  </section>

</main>
</body>
</html>
```